Business Card Design

I need a business card designed for my business.

The company name is Rowan Pellet Group

It has four brands underneath it. They are:
- RP Events
- RP Sports Tours
- RPG Management
- Bold Mosaic

I have attached all logo items, as well as our last business card.

I look forward to seeing your designs.

Industry/Entity Type

Business

Colors
eb1f27
0355a3

Requirements
Must have
• Our contact details as per the front page of our previous business card.

```html
<!DOCTYPE html>
<html lang="en">
<head>
<meta charset="utf-8">
<title>Rowan Pellet Group – Business Card</title>
<link rel="stylesheet" href="https://fonts.googleapis.com/css2?family=Arimo:wght@400;700&family=Cinzel:wght@700;900&display=swap">
<style>
  :root {
    --brand-red: #eb1f27;
    --brand-blue: #0355a3;
    --front-blue: #2b3cf2;
    --bar-blue: #1a22c8;
    --ink: #1a1a1a;
    --white: #ffffff;
    --back-red: #d8121c;
    --navy: #1b2f7a;
  }
  html, body {
    margin: 0;
    padding: 0;
    width: 1031px;
    height: 1200px;
    overflow: hidden;
    background: var(--white);
  }
  .canvas {
    position: relative;
    width: 1031px;
    height: 1200px;
    font-family: "Arimo", Arial, sans-serif;
  }
  .card {
    position: absolute;
    left: 0;
    width: 1031px;
    overflow: hidden;
    border: 2px solid #c9c9c9;
    box-sizing: border-box;
  }
  /* Front */
  .card--front {
    top: 0;
    height: 592px;
    background: linear-gradient(180deg, var(--white) 0%, var(--white) 30%, #c7ccf7 48%, #6d7af0 70%, var(--front-blue) 100%);
  }
  .brand-mark {
    position: absolute;
    left: 72px;
    top: 14px;
    width: 180px;
    height: 180px;
    border-radius: 50%;
    background: var(--brand-blue);
  }
  .brand-name {
    position: absolute;
    right: 50px;
    top: 72px;
    margin: 0;
    font-weight: 700;
    font-size: 60px;
    line-height: 1;
    color: var(--brand-blue);
    white-space: nowrap;
  }
  .brand-rule {
    position: absolute;
    left: 300px;
    right: 50px;
    top: 168px;
    height: 5px;
    background: var(--brand-red);
  }
  .person {
    position: absolute;
    left: 0;
    width: 1031px;
    text-align: center;
    font-family: "Cinzel", Georgia, serif;
    font-weight: 900;
    color: var(--ink);
    margin: 0;
    line-height: 1;
  }
  .person__name { top: 266px; font-size: 42px; }
  .person__role { top: 334px; font-size: 32px; }
  .address {
    position: absolute;
    left: 32px;
    top: 382px;
    margin: 0;
    font-style: normal;
    font-weight: 700;
    font-size: 29px;
    line-height: 40px;
    color: var(--white);
  }
  .phones {
    position: absolute;
    right: 32px;
    top: 400px;
    margin: 0;
    text-align: right;
    font-weight: 700;
    font-size: 29px;
    line-height: 40px;
    color: var(--white);
  }
  .contact-bar {
    position: absolute;
    left: 12px;
    right: 12px;
    bottom: 10px;
    height: 48px;
    background: var(--bar-blue);
    display: flex;
    justify-content: space-between;
    align-items: center;
    padding: 0 24px;
    box-sizing: border-box;
    font-weight: 700;
    font-size: 26px;
    color: var(--white);
  }
  /* Back */
  .card--back {
    top: 608px;
    height: 592px;
    background: linear-gradient(180deg, var(--white) 0%, var(--white) 22%, #f3b5b8 50%, #e8545b 75%, var(--back-red) 100%);
  }
  .brand-grid {
    position: absolute;
    left: 40px;
    right: 30px;
    top: 40px;
    height: 420px;
    display: grid;
    grid-template-columns: 1fr 1fr;
    grid-template-rows: 1fr 1fr;
    column-gap: 30px;
  }
  .sub-brand {
    margin: 0;
    display: flex;
    align-items: center;
    gap: 16px;
    font-weight: 700;
    font-size: 44px;
    line-height: 1;
    white-space: nowrap;
  }
  .sub-brand__dot {
    flex: none;
    width: 64px;
    height: 64px;
    border-radius: 50%;
    background: var(--navy);
  }
  .sub-brand--red { color: var(--back-red); }
  .sub-brand--navy { color: var(--navy); }
  .back-web {
    position: absolute;
    left: 0;
    bottom: 30px;
    width: 100%;
    margin: 0;
    text-align: center;
    font-weight: 700;
    font-size: 43px;
    color: var(--white);
  }
</style>
</head>
<body>
<main class="canvas">
  <section class="card card--front">
    <div class="brand-mark" aria-hidden="true"></div>
    <h1 class="brand-name">Rowan Pellet Group</h1>
    <div class="brand-rule" aria-hidden="true"></div>
    <p class="person person__name">Rowan Pellet</p>
    <p class="person person__role">Principal</p>
    <address class="address">PO Box 418<br>Belconnen ACT 2617<br>Australia</address>
    <p class="phones">+61 2 6000 4182<br>+61 400 555 318</p>
    <div class="contact-bar">
      <span>www.RowanPelletGroup.com.au</span>
      <span>Rowan@RowanPelletGroup.com.au</span>
    </div>
  </section>

  <section class="card card--back">
    <div class="brand-grid">
      <p class="sub-brand sub-brand--red"><span class="sub-brand__dot" aria-hidden="true"></span>RP Events</p>
      <p class="sub-brand sub-brand--red"><span class="sub-brand__dot" aria-hidden="true"></span>RP Sports Tours</p>
      <p class="sub-brand sub-brand--red"><span class="sub-brand__dot" aria-hidden="true"></span>Bold Mosaic</p>
      <p class="sub-brand sub-brand--navy"><span class="sub-brand__dot" aria-hidden="true"></span>RPG Management</p>
    </div>
    <p class="back-web">www.RowanPelletGroup.com.au</p>
  </section>
</main>
</body>
</html>
```